Business card design needed with logo

My business is called KVM Solutions & it is targeted towards mobile equipment maintenance in the Mining and civil industry. My work involves maintenance planning and maintenance management plus also supply tradespeople on a labour hire basis. We can provide from basic shut-down machine rebuild plans to complete rebuild services supply plans and labour to anywhere in Australia. I would like to use the colours Black, Red and Grey, I had done a desgin as attached but doesn't really explain what we do and gears don't embroider well onto shirts.
Updates

I also wanted to see the something replace the gears maybe just making the KVM lettering look a bit different or put together differently 

Hello I have extended the deadline by a few extra days as I would like to update details on the front of card, details below & can be put which ever way looks good;

Liam Fenwick
Director
0417263958
KVM@mailnest.com.au
www.kvmsolutions-demo.com.au

On the back of the card I would like to have the below printed;

Capable of providing, but not limited to, across Australia:
- Contract Maintenance Planning.
- Skilled Mobile Maintenance labour hire.
- New machine build specifications. 
- Plant risk assessments and inspections.
- Shut down and rebuild program planning.
- Preventative maintenance tasks, including build of materials lists, creation and review.

Target Market(s)

Contractors and companies that use small and large earthmoving and mining machines

Industry/Entity Type

Business

Contact Information for Business Card

Trading name is KVM Solutions
My name and title is
Liam Fenwick Director
0417 263 958
KVM@mailnest.com.au

Logo Text

KVM

```html
<!DOCTYPE html>
<html lang="en">
<head>
<meta charset="utf-8">
<title>KVM Solutions – Business Card</title>
<link rel="stylesheet" href="https://fonts.googleapis.com/css2?family=Open+Sans:wght@400;600;700;800&display=swap">
<style>
  :root {
    --bg: #ffffff;
    --card-top: #6c6c6e;
    --card-bottom: #505052;
    --red: #c0161e;
    --red-dark: #9e1016;
    --text-dark: #111111;
    --text-light: #f1f1f1;
    --text-muted: #dadada;
    --faint: rgba(20, 20, 20, 0.09);
  }
  * { box-sizing: border-box; margin: 0; padding: 0; }
  html, body {
    width: 1200px; height: 900px; overflow: hidden;
    background: var(--bg);
    font-family: "Open Sans", Arial, sans-serif;
  }
  .canvas {
    width: 1200px; height: 900px;
    display: flex; align-items: center; justify-content: center; gap: 44px;
  }
  .card {
    position: relative;
    width: 540px; height: 310px;
    border-radius: 22px;
    overflow: hidden;
    background: linear-gradient(180deg, var(--card-top), var(--card-bottom));
    box-shadow: 0 10px 28px rgba(0,0,0,0.18);
  }
  .card__band {
    position: absolute; left: 0; right: 0; bottom: 0; height: 44px;
    background: linear-gradient(180deg, var(--red), var(--red-dark));
  }

  /* Back */
  .services__heading {
    position: absolute; top: 26px; left: 0; right: 0;
    text-align: center; color: var(--red);
    font-size: 14.5px; font-weight: 600;
  }
  .services__watermark {
    position: absolute; top: 70px; right: 34px;
    font-size: 50px; line-height: 1.05; font-weight: 800;
    color: var(--faint); text-align: right;
    white-space: nowrap; z-index: 0;
  }
  .services__list {
    position: absolute; top: 66px; left: 22px; right: 20px; z-index: 1;
    list-style: none; color: var(--text-dark);
    font-size: 15px; line-height: 23px; font-weight: 600;
  }
  .services__list li { display: flex; align-items: flex-start; }
  .services__tick { flex: none; width: 14px; height: 14px; margin: 4px 3px 0 0; }

  /* Front */
  .brand {
    position: absolute; top: 64px; right: 40px;
    display: flex; align-items: center; gap: 14px;
  }
  .brand__mark { width: 22px; height: 22px; background: var(--red); border-radius: 50%; }
  .brand__name {
    font-size: 44px; font-weight: 800; color: var(--text-light);
    letter-spacing: 0.5px;
  }
  .person { position: absolute; left: 38px; top: 186px; }
  .person__name { font-size: 22px; font-weight: 600; color: var(--text-dark); }
  .person__title { font-size: 18px; font-weight: 600; color: var(--text-muted); margin-top: 4px; }
  .contact {
    position: absolute; right: 26px; top: 170px;
    list-style: none; color: var(--text-dark);
    font-size: 15px; line-height: 24px;
  }
  .contact li { display: flex; align-items: center; gap: 5px; }
  .contact__icon { width: 16px; height: 16px; flex: none; }
</style>
</head>
<body>
<main class="canvas">

  <section class="card card--back">
    <p class="services__heading">Capable of providing, but not limited to, across Australia</p>
    <div class="services__watermark" aria-hidden="true">KVM<br>Solutions</div>
    <ul class="services__list">
      <li><svg class="services__tick" viewBox="0 0 14 14"><path d="M1 9 L5 12 L13 2" fill="none" stroke="#c0161e" stroke-width="2.4" stroke-linecap="round"/></svg>Contract Maintenance Planning.</li>
      <li><svg class="services__tick" viewBox="0 0 14 14"><path d="M1 9 L5 12 L13 2" fill="none" stroke="#c0161e" stroke-width="2.4" stroke-linecap="round"/></svg>Skilled Mobile Maintenance labour hire.</li>
      <li><svg class="services__tick" viewBox="0 0 14 14"><path d="M1 9 L5 12 L13 2" fill="none" stroke="#c0161e" stroke-width="2.4" stroke-linecap="round"/></svg>New machine build specifications.</li>
      <li><svg class="services__tick" viewBox="0 0 14 14"><path d="M1 9 L5 12 L13 2" fill="none" stroke="#c0161e" stroke-width="2.4" stroke-linecap="round"/></svg>Plant risk assessments and inspections.</li>
      <li><svg class="services__tick" viewBox="0 0 14 14"><path d="M1 9 L5 12 L13 2" fill="none" stroke="#c0161e" stroke-width="2.4" stroke-linecap="round"/></svg>Shut down and rebuild program planning.</li>
      <li><svg class="services__tick" viewBox="0 0 14 14"><path d="M1 9 L5 12 L13 2" fill="none" stroke="#c0161e" stroke-width="2.4" stroke-linecap="round"/></svg><span>Preventative maintenance tasks,<br>including build of materials lists, creation and review.</span></li>
    </ul>
    <div class="card__band"></div>
  </section>

  <section class="card card--front">
    <div class="brand">
      <span class="brand__mark"></span>
      <span class="brand__name">KVM Solutions</span>
    </div>
    <div class="person">
      <p class="person__name">Liam Fenwick</p>
      <p class="person__title">Director</p>
    </div>
    <ul class="contact">
      <li><svg class="contact__icon" viewBox="0 0 16 16"><path d="M3 2h3l1.5 3.5-2 1.2a8 8 0 0 0 3.8 3.8l1.2-2L14 10v3a1 1 0 0 1-1 1A11 11 0 0 1 2 3a1 1 0 0 1 1-1z" fill="#c0161e"/></svg>0417263958</li>
      <li><svg class="contact__icon" viewBox="0 0 16 16"><rect x="1.5" y="3.5" width="13" height="9" fill="none" stroke="#c0161e" stroke-width="1.6"/><path d="M1.5 3.5 L8 9 L14.5 3.5" fill="none" stroke="#c0161e" stroke-width="1.6"/></svg>KVM@mailnest.com.au</li>
      <li><svg class="contact__icon" viewBox="0 0 16 16"><circle cx="8" cy="8" r="6.3" fill="none" stroke="#c0161e" stroke-width="1.6"/><ellipse cx="8" cy="8" rx="2.6" ry="6.3" fill="none" stroke="#c0161e" stroke-width="1.3"/><path d="M1.7 8h12.6" stroke="#c0161e" stroke-width="1.3"/></svg>www.kvmsolutions-demo.com.au</li>
    </ul>
    <div class="card__band"></div>
  </section>

</main>
</body>
</html>
```